I'm an electrician and the name of my company is called Brisk 'N' Bright Electrical. I require a professional business card that speaks to my clients, I also need it to be innovative and modern. We do maintenance & service work for domestic and commercial premises.

Industry/Entity Type

Electrical

Contact Information for Business Card

Must have the name of my company Brisk 'N' Bright Electrical, my name Darren Kolovich and my contact details 0427 318 592 and company email address Brisknbrightelectrical@quillpost.example and/or website Brisknbrightelectrical.example.au

Logo Text

Brisk 'N' Bright Electrical (If possible)

Colors
33a6d7
0592cd
3176b5

```html
<!DOCTYPE html>
<html lang="en">
<head>
<meta charset="utf-8">
<title>Brisk 'N' Bright Electrical — Business Card</title>
<link rel="stylesheet" href="https://fonts.googleapis.com/css2?family=Raleway:wght@700;800&family=Open+Sans:wght@400;600&display=swap">
<style>
  :root {
    --backdrop: #2b2b2d;
    --card: #1b1c1e;
    --card-deep: #111214;
    --teal: #17a6a8;
    --white: #ffffff;
    --rule: #8a8c8f;
  }
  * { box-sizing: border-box; margin: 0; padding: 0; }
  html, body { width: 1200px; height: 1108px; overflow: hidden; }
  body {
    background: var(--backdrop);
    position: relative;
    font-family: "Open Sans", sans-serif;
  }
  .card {
    position: absolute;
    top: 194px;
    width: 440px;
    height: 720px;
    border-radius: 30px;
    background: var(--card);
    overflow: hidden;
  }
  .card--front { left: 130px; }
  .card--back { left: 630px; }

  .brand {
    position: absolute;
    top: 130px;
    left: 0; right: 0;
    display: flex;
    flex-direction: column;
    align-items: center;
    gap: 22px;
  }
  .brand__mark {
    width: 64px; height: 64px;
    background: var(--teal);
  }
  .brand__name {
    font-family: "Raleway", sans-serif;
    font-weight: 800;
    font-size: 36px;
    line-height: 1.15;
    color: var(--white);
    text-align: center;
    text-transform: uppercase;
  }
  .holder {
    position: absolute;
    top: 440px; left: 0; right: 0;
    text-align: center;
    font-family: "Raleway", sans-serif;
    font-weight: 700;
    font-size: 30px;
    color: var(--teal);
    text-transform: uppercase;
  }
  .divider {
    position: absolute;
    top: 500px; left: 50px; right: 50px;
    display: flex;
    align-items: center;
    gap: 8px;
  }
  .divider__line { flex: 1; height: 1px; background: var(--rule); }
  .divider__icon {
    width: 38px; height: 38px;
    border-radius: 5px;
    background: var(--teal);
    display: flex; align-items: center; justify-content: center;
  }
  .contact {
    position: absolute;
    top: 558px; left: 0; right: 0;
    text-align: center;
    color: var(--white);
    text-transform: uppercase;
    font-size: 15px;
    line-height: 1.75;
    letter-spacing: 0.01em;
  }
  .contact__phone { font-size: 22px; font-weight: 600; line-height: 1.5; }
  .contact__web-domain { color: var(--teal); }

  .pattern {
    position: absolute; inset: 0;
    background: linear-gradient(150deg, #4a4b4e 0%, #2a2b2e 45%, var(--card-deep) 100%);
  }
  .back-brand {
    position: absolute;
    right: 70px; bottom: 180px;
    display: flex; align-items: center; gap: 10px;
  }
  .back-brand__mark { width: 22px; height: 22px; background: var(--teal); }
  .back-brand__name {
    font-family: "Raleway", sans-serif;
    font-weight: 800;
    font-size: 15px;
    color: var(--white);
    text-transform: uppercase;
  }
</style>
</head>
<body>
  <section class="card card--front">
    <div class="brand">
      <div class="brand__mark"></div>
      <div class="brand__name">Brisk 'N' Bright<br>Electrical</div>
    </div>

    <div class="holder">Darren Kolovich</div>

    <div class="divider">
      <span class="divider__line"></span>
      <span class="divider__icon">
        <svg width="22" height="22" viewBox="0 0 24 24" aria-label="Phone"><path fill="#1b1c1e" d="M6.6 10.8a15 15 0 0 0 6.6 6.6l2.2-2.2a1 1 0 0 1 1-.25 11.4 11.4 0 0 0 3.6.57 1 1 0 0 1 1 1V20a1 1 0 0 1-1 1A17 17 0 0 1 3 4a1 1 0 0 1 1-1h3.5a1 1 0 0 1 1 1c0 1.25.2 2.45.57 3.57a1 1 0 0 1-.25 1z"/></svg>
      </span>
      <span class="divider__icon">
        <svg width="22" height="22" viewBox="0 0 24 24" aria-label="Email"><rect x="3" y="5" width="18" height="14" rx="1" fill="none" stroke="#1b1c1e" stroke-width="2"/><path d="M3 6l9 7 9-7M3 18l7-6M21 18l-7-6" fill="none" stroke="#1b1c1e" stroke-width="1.6"/></svg>
      </span>
      <span class="divider__icon">
        <svg width="22" height="22" viewBox="0 0 24 24" aria-label="Website"><circle cx="12" cy="12" r="9" fill="#1b1c1e"/><ellipse cx="12" cy="12" rx="4" ry="9" fill="none" stroke="#17a6a8" stroke-width="1.4"/><path d="M3 12h18" stroke="#17a6a8" stroke-width="1.4"/></svg>
      </span>
      <span class="divider__line"></span>
    </div>

    <div class="contact">
      <div class="contact__phone">0427 318 592</div>
      <div class="contact__email">Brisknbrightelectrical@quillpost.example</div>
      <div class="contact__web">www.<span class="contact__web-domain">Brisknbrightelectrical</span>.example.au</div>
    </div>
  </section>

  <section class="card card--back">
    <div class="pattern" role="img" aria-label="Tiled gloss pattern of the company mark on black"></div>
    <div class="back-brand">
      <span class="back-brand__mark"></span>
      <span class="back-brand__name">Brisk 'N' Bright Electrical</span>
    </div>
  </section>
</body>
</html>
```